Granite, Brass and Shingle Roofing LLC needs a new business card

I need a new business card because I have a new address.
I do slate copper and tile roofs. My webpage is: www.granitebrassandshingleroofing.com

```html
<!DOCTYPE html>
<html lang="en">
<head>
<meta charset="utf-8">
<title>Granite, Brass and Shingle Roofing LLC — Business Card</title>
<link rel="stylesheet" href="https://fonts.googleapis.com/css2?family=Open+Sans:wght@400;600;700&display=swap">
<style>
  :root {
    --sky: #4f9ecf;
    --ink: #111418;
    --paper: #ffffff;
    --stage: #e9ebee;
    --text: #1d1f22;
  }
  * { box-sizing: border-box; margin: 0; padding: 0; }
  html, body {
    width: 1200px; height: 1000px; overflow: hidden;
    background: var(--stage);
    font-family: "Open Sans", Arial, sans-serif;
  }
  .sheet {
    width: 1200px; height: 1000px;
    display: flex; flex-direction: column;
    align-items: center; justify-content: center; gap: 60px;
  }
  .card {
    position: relative;
    width: 700px; height: 400px;
    border-radius: 22px;
    overflow: hidden;
    box-shadow: 0 10px 28px rgba(0,0,0,.18);
  }

  /* Back */
  .card--back { background: var(--sky); display: flex; align-items: center; justify-content: center; }
  .wordmark {
    display: flex; align-items: center; gap: 16px;
    color: var(--ink); font-weight: 700;
  }
  .wordmark__mark { width: 18px; height: 18px; background: var(--ink); flex: none; }
  .wordmark__name { font-size: 30px; line-height: 1.15; letter-spacing: .5px; }

  /* Front */
  .card--front { background: var(--paper); }
  .card--front .wordmark { position: absolute; top: 72px; left: 50%; transform: translateX(-50%); white-space: nowrap; }
  .card--front .wordmark__name { font-size: 24px; }
  .card--front .wordmark__mark { background: var(--sky); width: 16px; height: 16px; }

  .person {
    position: absolute; top: 178px; right: 388px;
    text-align: right;
  }
  .person__name { color: var(--sky); font-weight: 700; font-size: 25px; white-space: nowrap; }
  .person__role { color: var(--text); font-size: 18px; margin-top: 2px; }

  .divider { position: absolute; left: 332px; top: 180px; width: 1.5px; height: 92px; background: var(--sky); }

  .contact { position: absolute; left: 350px; top: 182px; list-style: none; }
  .contact li {
    display: flex; align-items: center; gap: 10px;
    font-size: 15px; color: var(--text); line-height: 30px; white-space: nowrap;
  }
  .contact svg { width: 16px; height: 16px; fill: var(--sky); flex: none; }

  .band {
    position: absolute; left: 0; right: 0; top: 300px; height: 56px;
    background: var(--sky);
    display: flex; align-items: center; justify-content: center;
    color: var(--paper); font-size: 19px; letter-spacing: .3px;
  }
</style>
</head>
<body>
<main class="sheet">

  <section class="card card--back" aria-label="Card back">
    <div class="wordmark">
      <span class="wordmark__mark"></span>
      <span class="wordmark__name">Granite, Brass &amp; Shingle Roofing</span>
    </div>
  </section>

  <section class="card card--front" aria-label="Card front">
    <div class="wordmark">
      <span class="wordmark__mark"></span>
      <span class="wordmark__name">Granite, Brass &amp; Shingle Roofing</span>
    </div>

    <div class="person">
      <p class="person__name">Laszlo (Leo) Varga</p>
      <p class="person__role">Owner</p>
    </div>

    <div class="divider"></div>

    <ul class="contact">
      <li>
        <svg viewBox="0 0 24 24" aria-hidden="true"><path d="M6.6 10.8a15.5 15.5 0 0 0 6.6 6.6l2.2-2.2a1 1 0 0 1 1-.25 11.4 11.4 0 0 0 3.6.57 1 1 0 0 1 1 1V20a1 1 0 0 1-1 1A17 17 0 0 1 3 4a1 1 0 0 1 1-1h3.5a1 1 0 0 1 1 1c0 1.25.2 2.45.57 3.57a1 1 0 0 1-.25 1z"/></svg>
        (440) 555-0187
      </li>
      <li>
        <svg viewBox="0 0 24 24" aria-hidden="true"><path d="M2 5h20v14H2zm2 2v.5l8 5 8-5V7l-8 5z"/></svg>
        info@granitebrassandshingleroofing.com
      </li>
      <li>
        <svg viewBox="0 0 24 24" aria-hidden="true"><path d="M12 2a10 10 0 1 0 0 20 10 10 0 0 0 0-20zm0 2c.9 0 2.3 2 2.8 5H9.2C9.7 6 11.1 4 12 4zm-3 7h6a18 18 0 0 1 0 2H9a18 18 0 0 1 0-2zm.2 4h5.6c-.5 3-1.9 5-2.8 5s-2.3-2-2.8-5z"/></svg>
        www.granitebrassandshingleroofing.com
      </li>
    </ul>

    <div class="band">2870 Millbrook Rd Millbrook, OH 44390</div>
  </section>

</main>
</body>
</html>
```